Web Design Project

We need a website for a new public relations firm offering PR, advertising, media buying, design and social media. Target clients are professional service firms such as lawyers or CPAs. Looks should be clean and look expensive.

Target Market(s)

Professional service firms. Think business to business companies like consultancy firms.

Industry/Entity Type

Professional Service

Colors

Designer to choose colors to be used in the design.

Requirements
Must have
• Site pages for the purpose of design will include Home, Services, Experience, Bios and Contact Us

```html
<!DOCTYPE html>
<html lang="en">
<head>
<meta charset="utf-8">
<title>KLR — Marketing · PR · Advertising</title>
<link href="https://fonts.googleapis.com/css2?family=Cinzel:wght@400;500&family=Open+Sans:wght@300;400&family=Arimo:wght@400;700&display=swap" rel="stylesheet">
<style>
:root{
  --slate:#3a434d;
  --slate-bar:#5b6168;
  --footer:#dde0e8;
  --logo:#8a8c90;
  --nav:#7c7f84;
  --body-text:#5c6b88;
  --heading:#4a5262;
  --green:#93c13f;
  --white:#ffffff;
  --dark-btn:#2f353c;
}
*{margin:0;padding:0;box-sizing:border-box}
html,body{width:960px;height:1200px;overflow:hidden;background:var(--white)}
body{position:relative;font-family:'Arimo',Arial,sans-serif}
.abs{position:absolute}

/* header */
.brand{left:90px;top:14px;width:160px}
.brand-name{font-family:'Cinzel',serif;font-size:50px;line-height:50px;color:var(--logo);letter-spacing:2px}
.brand-tag{font-family:'Cinzel',serif;font-size:8px;color:#333;letter-spacing:.6px;margin-top:4px}
.main-nav{left:350px;top:34px;display:flex;gap:0}
.main-nav a{font-family:'Cinzel',serif;font-size:11.5px;color:var(--nav);text-decoration:none;margin-right:37px}
.main-nav a:last-child{margin-right:0}

/* hero */
.hero{left:0;top:94px;width:960px;height:360px;background:linear-gradient(100deg,#cfd6dc 0%,#eef1f3 30%,#e6eaec 50%,#f3f4f4 62%,#c9cf8f 78%,#eef0ee 100%)}
.hero-caption{left:95px;top:398px;width:769px;height:56px;background:rgba(80,86,94,.88)}
.arrow{width:28px;height:28px}
.caption-title{left:144px;top:410px;font-family:'Cinzel',serif;font-size:17px;color:var(--white);letter-spacing:.5px}
.caption-text{left:146px;top:429px;font-family:'Open Sans',sans-serif;font-size:11px;color:#e0e2e4}
.learn-more{left:706px;top:408px;width:103px;height:37px;background:#eceeef;color:#555b62;font-family:'Open Sans',sans-serif;font-weight:400;font-size:11.5px;line-height:37px;text-align:center;letter-spacing:.3px}

/* services band */
.services{left:0;top:454px;width:960px;height:166px;background:var(--slate)}
.service{top:480px;width:230px}
.service-icon{display:block;margin:0 auto 10px}
.service h3{font-family:'Cinzel',serif;font-weight:400;font-size:12.5px;color:var(--white);text-align:center;letter-spacing:.5px;margin-bottom:13px}
.service p{font-size:9.5px;line-height:11.7px;color:#dfe2e6;padding-left:2px}

/* content */
.col{top:677px;width:235px}
.col h2{font-family:'Open Sans',sans-serif;font-weight:300;font-size:20px;color:var(--heading);margin-bottom:10px}
.col p{font-size:11px;line-height:13.4px;color:var(--body-text)}
.col p+p{margin-top:13px}
.thumb{float:left;width:136px;height:92px;margin:0 7px 6px 0}
.read-more{display:inline-block;margin-top:13px;width:103px;height:36px;background:var(--green);color:var(--white);font-size:11px;line-height:36px;text-align:center}

/* newsletter */
.newsletter{left:0;top:955px;width:960px;height:143px;background:var(--slate)}
.news-title{left:0;top:977px;width:960px;text-align:center;font-family:'Open Sans',sans-serif;font-weight:300;font-size:19px;color:var(--white)}
.news-text{left:0;top:1006px;width:960px;text-align:center;font-family:'Open Sans',sans-serif;font-size:9.5px;color:#c8ccd2}
.email{left:356px;top:1034px;width:186px;height:25px;background:var(--white);font-size:11px;color:#444;line-height:25px;padding-left:9px}
.submit{left:542px;top:1034px;width:63px;height:25px;background:var(--dark-btn);color:var(--white);font-size:11px;line-height:25px;text-align:center}

/* footer */
.footer{left:0;top:1098px;width:960px;height:102px;background:var(--footer)}
.footer-brand{left:102px;top:1113px}
.social{left:428px;top:1124px;display:flex;gap:10px}
.social span{width:16px;height:16px;border-radius:50%;background:#8b9099;display:block}
.copyright{left:400px;top:1152px;font-size:9.5px;color:#444}
.address{left:723px;top:1120px;font-size:11px;line-height:13.5px;color:#555}
.address strong{color:#555;font-weight:700}
.pin{left:707px;top:1122px}
</style>
</head>
<body>

<header>
  <div class="abs brand">
    <div class="brand-name">KLR</div>
    <div class="brand-tag">Marketing · PR · Advertising</div>
  </div>
  <nav class="abs main-nav">
    <a href="#">Home</a><a href="#">Services</a><a href="#">Experiences</a><a href="#">Bios</a><a href="#">Latest News</a><a href="#">Contact Us</a>
  </nav>
</header>

<section>
  <div class="abs hero" role="img" aria-label="Photo of four business people meeting in a bright modern office lounge with green chairs"></div>
  <div class="abs hero-caption"></div>
  <svg class="abs arrow" style="left:104px;top:413px" viewBox="0 0 28 28"><circle cx="14" cy="14" r="12" fill="none" stroke="#fff" stroke-width="2.4"/><path d="M16 8l-6 6 6 6" fill="none" stroke="#fff" stroke-width="2.6"/></svg>
  <div class="abs caption-title">OUR EXPERIENCE</div>
  <div class="abs caption-text">Duis aute irure dolor in reprehenderit in voluptate&nbsp; velit esse cillum dolore eu fugiat nulla pariatur.</div>
  <div class="abs learn-more">LEARN MORE ›</div>
  <svg class="abs arrow" style="left:824px;top:414px" viewBox="0 0 28 28"><circle cx="14" cy="14" r="12" fill="none" stroke="#fff" stroke-width="2.4"/><path d="M12 8l6 6-6 6" fill="none" stroke="#fff" stroke-width="2.6"/></svg>
</section>

<section>
  <div class="abs services"></div>
  <div class="abs service" style="left:103px">
    <svg class="service-icon" width="42" height="42" viewBox="0 0 42 42" role="img" aria-label="PR and advertising icon"><circle cx="21" cy="21" r="17" fill="none" stroke="#fff" stroke-width="2"/><path d="M12 27l8-7 5 4 8-9" fill="none" stroke="#fff" stroke-width="2.4"/></svg>
    <h3>PR &amp; ADVERTISING</h3>
    <p>Lorem ipsum dolor sit amet, consectetur adipisicing elit, sed do eiusmod tempor incididunt ut labore et dolore magna aliqua.</p>
  </div>
  <div class="abs service" style="left:366px">
    <svg class="service-icon" width="42" height="42" viewBox="0 0 42 42" role="img" aria-label="Media buying icon"><circle cx="21" cy="21" r="17" fill="none" stroke="#fff" stroke-width="2"/><circle cx="21" cy="21" r="8" fill="#fff"/></svg>
    <h3>MEDIA BUYING</h3>
    <p>Duis aute irure dolor in reprehenderit in voluptate velit esse cillum dolore eu fugiat nulla pariatur. Excepteur sint occaecat cupidatat non proident.</p>
  </div>
  <div class="abs service" style="left:628px">
    <svg class="service-icon" width="42" height="42" viewBox="0 0 42 42" role="img" aria-label="Social media icon"><circle cx="21" cy="21" r="17" fill="none" stroke="#fff" stroke-width="2"/><circle cx="13" cy="21" r="3" fill="#fff"/><circle cx="21" cy="21" r="3" fill="#fff"/><circle cx="29" cy="21" r="3" fill="#fff"/></svg>
    <h3>SOCIAL MEDIA</h3>
    <p>Sed ut perspiciatis, unde omnis iste natus error sit voluptatem accusantium doloremque laudantium, totam rem aperiam eaque ipsa, quae ab illo.</p>
  </div>
</section>

<main>
  <article class="abs col" style="left:99px">
    <h2>Who Choose Us</h2>
    <p>Lorem ipsum dolor sit amet, consectetur adipisicing elit, sed do eiusmod tempor incididunt ut labore et dolore magna aliqua.</p>
    <p>Ut enim ad minim veniam, quis nostrud exercitation ullamco laboris nisi ut aliquip ex ea commodo consequat. Duis aute irure dolor in reprehenderit in voluptate velit esse cillum dolore eu fugiat nulla pariatur.</p>
    <a class="read-more" style="margin-left:-1px">read more</a>
  </article>
  <article class="abs col" style="left:358px;width:250px">
    <h2>Experiences</h2>
    <div class="thumb" role="img" aria-label="Photo of three business people in suits" style="background:linear-gradient(90deg,#c9ccd0,#9aa0a8 50%,#c4c7cb)"></div>
    <p>Lorem ipsum dolor sit amet, consectetur adipisicing elit, sed do eiusmod tempor incididunt ut labore et dolore magna aliqua.</p>
    <p style="clear:both;margin-top:0">Ut enim ad minim veniam, quis nostrud exercitation ullamco laboris nisi ut aliquip ex ea commodo consequat. Duis aute irure dolor in reprehenderit in voluptate velit esse cillum dolore eu fugiat nulla pariatur.</p>
  </article>
  <article class="abs col" style="left:619px;width:250px">
    <h2>About KLR</h2>
    <div class="thumb" role="img" aria-label="Photo of colleagues in a meeting around a table" style="background:linear-gradient(90deg,#d8d2c8,#b7b9bd 50%,#6a6e74)"></div>
    <p>Lorem ipsum dolor sit amet, consectetur adipisicing elit, sed do eiusmod tempor incididunt ut labore et dolore magna aliqua.</p>
    <p style="clear:both;margin-top:0">Ut enim ad minim veniam, quis nostrud exercitation ullamco laboris nisi ut aliquip ex ea commodo consequat. Duis aute irure dolor in reprehenderit in voluptate velit esse cillum dolore eu fugiat nulla pariatur.</p>
  </article>
</main>

<section>
  <div class="abs newsletter"></div>
  <div class="abs news-title">SUBSCRIBE TO NEWSLETTER</div>
  <div class="abs news-text">Lorem ipsum dolor sit amet, consectetur adipisicing elit, sed do eiusmod tempor incididunt ut labore</div>
  <div class="abs email">enter email</div>
  <div class="abs submit">submit</div>
</section>

<footer>
  <div class="abs footer"></div>
  <div class="abs footer-brand">
    <div class="brand-name">KLR</div>
    <div class="brand-tag">Marketing · PR · Advertising</div>
  </div>
  <div class="abs social"><span></span><span></span><span></span><span></span></div>
  <div class="abs copyright">Copyright © 2014 | Terms | Privacy</div>
  <svg class="abs pin" width="10" height="14" viewBox="0 0 10 14"><path d="M5 0a5 5 0 0 1 5 5c0 3.5-5 9-5 9S0 8.5 0 5a5 5 0 0 1 5-5z" fill="#555"/><circle cx="5" cy="5" r="2" fill="#dde0e8"/></svg>
  <div class="abs address">4120 Harbour Lane,<br>BRISTOL, BS 21 4QT<br><strong>CALL US: 1 800 555 0142</strong></div>
</footer>

</body>
</html>
```